Business Cards, Stationary, Fax, Envelopes
Larkspur Valley Wellness Pharmacy and Home Care
Professional
Dale Corvin, PharmD
President
418 Quarry Lane
Phillipsburg, KS 67492-2741
dcorvin@larkspurvalleyrx.example
www.larkspurvalleyrx.example
Our logo is the one with the Blue/Green Rx/Sun symbol. The additional logo provided is to be used ONLY for the back of the business card (read back of business card section).
We have not introduced the new logo to our business yet, so fonts are still changable.
The fonts that the attached logo uses are Versailles LT Bold, Versailles LT and Helvetica NeueLT Std. HOWEVER, we would love to consider other types of fonts if you have ideas that might look better, please try them.
The "Pharmacy and Home Care" could be in black if that looked better than gray for your design.
Thank you!
On the back of the card, please use the round emblem that says PHARMACY AND HOME CARE EXPERTS and then replace the middle of the emblem with our logo Rx/Sun symbol. So this is: Our symbol with the PHARMACY AND HOME CARE EXPERTS surrounding it. Please disregard the Larkspur Valley Wellness part of this particular logo. Thank you!
This is the emblem for the BACK OF THE CARD - please see brief for instructions.

```html
<!DOCTYPE html>
<html lang="en">
<head>
<meta charset="utf-8">
<title>Larkspur Valley Wellness – Stationery Set</title>
<link href="https://fonts.googleapis.com/css2?family=Crimson+Pro:wght@700&family=Open+Sans:wght@400;600&display=swap" rel="stylesheet">
<style>
:root{
  --bg:#e9e6e1;
  --paper:#ffffff;
  --green:#1f8a3c;
  --green-dark:#0f6a2e;
  --blue:#1a5fa8;
  --blue-dark:#123f7a;
  --grey:#6d6f71;
  --ink:#333;
}
*{box-sizing:border-box;margin:0;padding:0}
html,body{width:1200px;height:485px;overflow:hidden;background:var(--bg);font-family:"Open Sans",Arial,sans-serif;color:var(--ink)}
.canvas{position:relative;width:1200px;height:485px}
.piece{position:absolute;background:var(--paper);box-shadow:0 2px 6px rgba(0,0,0,.18);overflow:hidden}
.wave{position:absolute;left:0;bottom:0;width:100%}
.logo{display:flex;align-items:center;gap:6px}
.logo-dot{flex:none;border-radius:50%;background:var(--blue)}
.logo-text{line-height:1}
.logo-name{font-family:"Crimson Pro",Georgia,serif;font-weight:700;color:var(--blue);text-transform:uppercase;letter-spacing:.02em;display:block;white-space:nowrap}
.logo-sub{display:block;color:var(--grey);font-size:.55em;margin-top:2px;white-space:nowrap}

/* folder */
.folder-inner{left:19px;top:72px;width:220px;height:324px}
.folder-cover{left:239px;top:72px;width:218px;height:324px;background:linear-gradient(170deg,#fff 0 28%,var(--green) 28% 100%)}
.folder-cover .logo{position:absolute;left:14px;top:18px;font-size:12px}
.folder-cover .logo-dot{width:24px;height:24px}
.folder-tagline{position:absolute;left:14px;top:272px;color:#fff;font-size:11px}
.folder-pocket{position:absolute;top:396px;height:72px;width:205px;background:var(--paper);box-shadow:0 2px 5px rgba(0,0,0,.15);display:flex;align-items:flex-start;justify-content:center;padding-top:10px}
.pocket-left{left:19px;clip-path:polygon(0 0,100% 0,100% 40%,88% 100%,0 100%)}
.pocket-right{left:248px;clip-path:polygon(0 0,100% 0,100% 100%,10% 100%,0 40%)}
.emblem{width:24px;height:24px;border-radius:50%;background:var(--green)}

/* letterheads */
.letterhead{top:163px;width:214px;height:305px}
.fax{left:468px}
.letter{left:700px}
.letterhead .logo{position:absolute;left:12px;top:12px;font-size:10px}
.letterhead .logo-dot{width:18px;height:18px}
.fax-title{position:absolute;right:14px;top:52px;font-size:10px;font-weight:600;color:var(--green-dark)}
.fax-table{position:absolute;left:12px;top:68px;width:190px;border-collapse:collapse;font-size:6px;color:var(--grey)}
.fax-table td{border:1px solid #bbb;height:10px;padding:0 3px;width:25%}
.fax-checks{position:absolute;left:12px;top:124px;display:flex;gap:8px;font-size:5.5px;color:var(--grey)}
.fax-checks span::before{content:"";display:inline-block;width:5px;height:5px;border:1px solid #999;margin-right:2px;vertical-align:-1px}

/* small items */
.slip-small{left:528px;top:24px;width:132px;height:84px}
.slip-small .logo{position:absolute;left:8px;top:8px;font-size:7px}
.slip-small .logo-dot{width:12px;height:12px}
.card{width:90px;height:40px;font-size:5px}
.card .logo{position:absolute;left:5px;top:4px;font-size:4.5px}
.card .logo-dot{width:9px;height:9px}
.card-front{left:715px;top:24px}
.card-blue{background:linear-gradient(160deg,var(--blue),var(--blue-dark))}
.card-blue-a{left:809px;top:24px}
.card-blue-b{left:715px;top:72px}
.card-back{left:809px;top:72px;display:flex;align-items:center;justify-content:center}
.card-back .emblem{width:22px;height:22px}
.card-details{position:absolute;left:5px;top:7px;color:#fff;line-height:1.25;font-size:4.5px;white-space:nowrap}
.card-details strong{font-weight:600;font-size:5px}

.dl{left:924px;width:252px;height:84px}
.dl-a{top:24px}
.dl-b{top:132px}
.dl .logo{position:absolute;left:10px;top:10px;font-size:9px}
.dl .logo-dot{width:15px;height:15px}
.dl-address{position:absolute;right:10px;top:12px;font-size:5.5px;color:var(--grey);text-align:right;line-height:1.4}

/* envelopes */
.envelope{left:924px;width:252px;height:56px;background:var(--paper)}
.env-1{top:232px}
.env-2{top:296px;background:linear-gradient(180deg,var(--blue) 0 45%,#fff 45%)}
.env-3{top:360px;background:linear-gradient(0deg,var(--green) 0 45%,#fff 45%)}
.env-label{position:absolute;left:50%;transform:translateX(-50%);font-family:"Crimson Pro",Georgia,serif;font-weight:700;font-size:7px;color:var(--blue);text-transform:uppercase;white-space:nowrap}
.env-2 .env-label{top:32px}
.env-3 .env-label{top:12px}
</style>
</head>
<body>
<main class="canvas">

  <section class="piece folder-inner">
    <svg class="wave" viewBox="0 0 100 30" preserveAspectRatio="none" height="60"><path d="M0 14 Q50 2 100 10 V30 H0Z" fill="var(--green)"/><path d="M0 12 Q50 0 100 8" stroke="var(--blue)" stroke-width="1" fill="none"/></svg>
  </section>
  <section class="piece folder-cover">
    <div class="logo"><span class="logo-dot"></span><span class="logo-text"><span class="logo-name">Larkspur Valley Wellness</span><span class="logo-sub">Pharmacy and Home Care</span></span></div>
    <p class="folder-tagline">Pharmacy and Home Care Experts</p>
  </section>
  <div class="folder-pocket pocket-left"><span class="emblem"></span></div>
  <div class="folder-pocket pocket-right"><span class="emblem"></span></div>

  <section class="piece letterhead fax">
    <div class="logo"><span class="logo-dot"></span><span class="logo-text"><span class="logo-name">Larkspur Valley Wellness</span><span class="logo-sub">Pharmacy and Home Care</span></span></div>
    <p class="fax-title">FAX</p>
    <table class="fax-table">
      <tr><td>To:</td><td></td><td>From:</td><td></td></tr>
      <tr><td>Fax:</td><td></td><td>Pages:</td><td></td></tr>
      <tr><td>Phone:</td><td></td><td>Date:</td><td></td></tr>
      <tr><td>Re:</td><td></td><td>CC:</td><td></td></tr>
    </table>
    <div class="fax-checks"><span>Urgent</span><span>Review</span><span>Comment</span><span>Reply</span><span>Recycle</span></div>
    <svg class="wave" viewBox="0 0 100 30" preserveAspectRatio="none" height="40"><path d="M0 16 Q50 4 100 12 V30 H0Z" fill="var(--green)"/><path d="M0 13 Q50 1 100 9" stroke="var(--blue)" stroke-width="1" fill="none"/></svg>
  </section>

  <section class="piece letterhead letter">
    <div class="logo"><span class="logo-dot"></span><span class="logo-text"><span class="logo-name">Larkspur Valley Wellness</span><span class="logo-sub">Pharmacy and Home Care</span></span></div>
    <svg class="wave" viewBox="0 0 100 30" preserveAspectRatio="none" height="40"><path d="M0 16 Q50 4 100 12 V30 H0Z" fill="var(--green)"/><path d="M0 13 Q50 1 100 9" stroke="var(--blue)" stroke-width="1" fill="none"/></svg>
  </section>

  <section class="piece slip-small">
    <div class="logo"><span class="logo-dot"></span><span class="logo-text"><span class="logo-name">Larkspur Valley Wellness</span></span></div>
    <svg class="wave" viewBox="0 0 100 30" preserveAspectRatio="none" height="18"><path d="M0 16 Q50 4 100 12 V30 H0Z" fill="var(--green)"/></svg>
  </section>

  <section class="piece card card-front">
    <div class="logo"><span class="logo-dot"></span><span class="logo-text"><span class="logo-name">Larkspur Valley Wellness</span></span></div>
    <svg class="wave" viewBox="0 0 100 30" preserveAspectRatio="none" height="10"><path d="M0 16 Q50 4 100 12 V30 H0Z" fill="var(--green)"/></svg>
  </section>
  <section class="piece card card-blue card-blue-a">
    <div class="card-details"><strong>Dale Corvin, PharmD</strong><br>President<br>418 Quarry Lane<br>Phillipsburg, KS 67492-2741<br>dcorvin@larkspurvalleyrx.example</div>
  </section>
  <section class="piece card card-blue card-blue-b">
    <div class="card-details"><strong>Dale Corvin, PharmD</strong><br>President<br>418 Quarry Lane<br>Phillipsburg, KS 67492-2741<br>www.larkspurvalleyrx.example</div>
  </section>
  <section class="piece card card-back"><span class="emblem"></span></section>

  <section class="piece dl dl-a">
    <div class="logo"><span class="logo-dot"></span><span class="logo-text"><span class="logo-name">Larkspur Valley Wellness</span><span class="logo-sub">Pharmacy and Home Care</span></span></div>
    <p class="dl-address">418 Quarry Lane<br>Phillipsburg, KS 67492-2741<br>www.larkspurvalleyrx.example</p>
    <svg class="wave" viewBox="0 0 100 30" preserveAspectRatio="none" height="18"><path d="M0 16 Q50 4 100 12 V30 H0Z" fill="var(--green)"/><path d="M0 13 Q50 1 100 9" stroke="var(--blue)" stroke-width="1" fill="none"/></svg>
  </section>
  <section class="piece dl dl-b">
    <div class="logo"><span class="logo-dot"></span><span class="logo-text"><span class="logo-name">Larkspur Valley Wellness</span><span class="logo-sub">Pharmacy and Home Care</span></span></div>
    <svg class="wave" viewBox="0 0 100 30" preserveAspectRatio="none" height="18"><path d="M0 16 Q50 4 100 12 V30 H0Z" fill="var(--green)"/></svg>
  </section>

  <section class="piece envelope env-1">
    <svg width="252" height="56" viewBox="0 0 252 56"><path d="M0 0 L126 30 L252 0" fill="none" stroke="#ccc"/></svg>
  </section>
  <section class="piece envelope env-2"><p class="env-label">Larkspur Valley Wellness</p></section>
  <section class="piece envelope env-3"><p class="env-label">Larkspur Valley Wellness</p></section>

</main>
</body>
</html>
```